Business Card Design Project

We need a redesign of our business card.
We are a Consulting Property Developer called The Selwick Group
Updates

Thank you all for submissions. Just waiting on managment to decide.

Thank you,

Dorinda

Industry/Entity Type

Business

Requirements
Must have
• we like having the SG a focus in the back ground or on the side
Selwick is our company colour

the wording - property development
and - premium accommodation

our website www.selwickgroup.com.au

persons name
title

p: 1300 582914 f: 1300 582917 m: 0419358027
PO Box 2817, Brackenvale Qld 4215
e: admin@selwickgroup.com.au

```html
<!DOCTYPE html>
<html lang="en">
<head>
<meta charset="utf-8">
<title>The Selwick Group – Business Card</title>
<link rel="stylesheet" href="https://fonts.googleapis.com/css2?family=PT+Sans:ital,wght@0,400;1,400&display=swap">
<style>
  :root {
    --selwick: #9b1b30;
    --grey: #9d9d9f;
    --ink: #1a1a1a;
    --frame: #7a7a7a;
    --watermark: rgba(155, 27, 48, 0.07);
    --page: #ffffff;
  }
  * { margin: 0; padding: 0; box-sizing: border-box; }
  html, body {
    width: 1200px;
    height: 900px;
    overflow: hidden;
    background: var(--page);
  }
  .canvas { position: relative; width: 1200px; height: 900px; }
  .business-card {
    position: absolute;
    left: 350px;
    top: 310px;
    width: 500px;
    height: 279px;
    border: 2px solid var(--frame);
    background: var(--page);
    overflow: hidden;
    font-family: "PT Sans", sans-serif;
  }
  .card-art { position: absolute; inset: 0; }
  .brand-name {
    position: absolute;
    left: 148px;
    top: 14px;
    font-size: 40px;
    line-height: 40px;
    font-weight: 400;
    color: var(--grey);
    letter-spacing: -0.5px;
    white-space: nowrap;
  }
  .text-line {
    position: absolute;
    font-style: italic;
    white-space: nowrap;
  }
  .tagline { color: var(--selwick); font-size: 19px; line-height: 19px; }
  .tagline--development { left: 127px; top: 72px; }
  .tagline--accommodation { left: 124px; top: 90px; }
  .person { color: var(--ink); font-size: 17px; line-height: 17px; }
  .person--name { left: 118px; top: 128px; }
  .person--title { left: 115px; top: 152px; }
  .contact { color: var(--ink); font-size: 17px; line-height: 17px; }
  .contact--phones { left: 105px; top: 197px; }
  .contact--postal { left: 101px; top: 220px; }
  .contact--email { left: 98px; top: 244px; }
</style>
</head>
<body>
<main class="canvas">
  <section class="business-card" aria-label="The Selwick Group business card">
    <svg class="card-art" width="500" height="279" viewBox="0 0 500 279" aria-hidden="true">
      <circle class="backdrop-mark" cx="230" cy="150" r="100" fill="var(--watermark)"/>
      <circle class="brand-dot" cx="62" cy="36" r="18" fill="var(--selwick)"/>
      <line class="brand-divider" x1="138" y1="12" x2="138" y2="60" stroke="var(--grey)" stroke-width="1"/>
      <line class="header-rule" x1="22" y1="59" x2="442" y2="59" stroke="var(--grey)" stroke-width="1"/>
    </svg>

    <h1 class="brand-name">The Selwick Group</h1>

    <p class="text-line tagline tagline--development">property development</p>
    <p class="text-line tagline tagline--accommodation">premium accommodation</p>

    <p class="text-line person person--name">persons name</p>
    <p class="text-line person person--title">title</p>

    <p class="text-line contact contact--phones">p: 1300 582914 f: 1300 582917 m: 0419358027</p>
    <p class="text-line contact contact--postal">PO Box 2817, Brackenvale Qld 4215</p>
    <p class="text-line contact contact--email">e: admin@selwickgroup.com.au</p>
  </section>
</main>
</body>
</html>
```